MS Word Template for Proposals and RFP

Looking for a nice looking graphic template in MS Word. We will use this to make proposals and answer RFPs. Looking for something that will match our company brand, but give a fresh, up-to-date look and feel. There are a few pictures of a template I like. I don't necessarily like that logo - looks too "kid like" for business, but I really like how clean and organized it is. Most proposals and RFP responses are looooooonnnngggg and boring - need something that someone can look through and find what they are looking for quickly and easily.
Updates

Can't wait to see your designs!

Target Market(s)

School districts and other governmental employers

Industry/Entity Type

Business

Requirements
Must have
• Must include sample table of contents, section dividers, charts, graphs and tables that we customized based on the content. The goal is for it to look simple, clean, compelling - organized so it's easy to read, easy to find your way around - good headers, charts, flow charts, tables.... etc. Looking to have 5-10 template pages that we can use to put together and entire portfolio.
Should not have
• No "cutsie" comic sans/apple for the teacher kind of stuff - we are selling employee benefits to schools and other governmental entities. Should be more serious and conservative but also look compelling and draw in the reader.

```html
<!DOCTYPE html>
<html lang="en">
<head>
<meta charset="utf-8">
<title>Table of Contents – Proposal Template</title>
<link href="https://fonts.googleapis.com/css2?family=Source+Sans+3:wght@400;600&display=swap" rel="stylesheet">
<style>
  :root {
    --frame-blue: #1e74bf;
    --title-blue: #1f70b8;
    --entry-blue: #2072b9;
    --page-num: #2b3d8f;
    --rule: #d3e3f1;
    --wash-top: #ffffff;
    --wash-mid: #bcd7ed;
    --footer-rule: #e6e6e6;
    --brand-grey: #8c8f94;
  }
  * { margin: 0; padding: 0; box-sizing: border-box; }
  html, body {
    width: 928px;
    height: 1200px;
    overflow: hidden;
    background: var(--frame-blue);
  }
  .page {
    position: relative;
    width: 928px;
    height: 1200px;
    background: var(--frame-blue);
    font-family: "Source Sans 3", "Source Sans Pro", Arial, sans-serif;
  }
  .sheet {
    position: absolute;
    left: 32px;
    top: 31px;
    width: 863px;
    height: 1144px;
    background: linear-gradient(
      to bottom,
      var(--wash-top) 0%,
      #eaf2fa 16%,
      #d3e5f3 35%,
      var(--wash-mid) 46%,
      #d3e5f3 60%,
      #eaf2f9 82%,
      var(--wash-top) 92%,
      var(--wash-top) 100%
    );
  }
  .page-title {
    position: absolute;
    left: 27px;
    top: 54px;
    font-size: 43px;
    font-weight: 600;
    color: var(--title-blue);
    letter-spacing: -0.2px;
  }
  .toc {
    position: absolute;
    left: 86px;
    top: 337px;
    width: 664px;
    list-style: none;
  }
  .toc-entry {
    display: flex;
    justify-content: space-between;
    align-items: flex-end;
    height: 45.5px;
    padding: 0 7px 6px 6px;
    border-bottom: 1px solid var(--rule);
    font-size: 22px;
    font-weight: 600;
  }
  .toc-label { color: var(--entry-blue); }
  .toc-page { color: var(--page-num); }
  .footer {
    position: absolute;
    left: 14px;
    right: 14px;
    top: 1051px;
    height: 93px;
    border-top: 1px solid var(--footer-rule);
    display: flex;
    justify-content: center;
    align-items: center;
  }
  .brand-name {
    font-size: 26px;
    font-weight: 400;
    color: var(--brand-grey);
    letter-spacing: 1.5px;
    text-transform: uppercase;
  }
</style>
</head>
<body>
  <div class="page">
    <main class="sheet">
      <h1 class="page-title">Table of Contents</h1>
      <ol class="toc">
        <li class="toc-entry"><span class="toc-label">Lorem ipsum dolor sit</span><span class="toc-page">01</span></li>
        <li class="toc-entry"><span class="toc-label">Lorem ipsum</span><span class="toc-page">04</span></li>
        <li class="toc-entry"><span class="toc-label">Lorem ipsum dolor sit</span><span class="toc-page">06</span></li>
        <li class="toc-entry"><span class="toc-label">Lorem ipsum</span><span class="toc-page">07</span></li>
        <li class="toc-entry"><span class="toc-label">Lorem ipsum dolor sit</span><span class="toc-page">12</span></li>
        <li class="toc-entry"><span class="toc-label">Lorem ipsum</span><span class="toc-page">14</span></li>
        <li class="toc-entry"><span class="toc-label">Lorem ipsum dolor sit</span><span class="toc-page">15</span></li>
        <li class="toc-entry"><span class="toc-label">Lorem ipsum</span><span class="toc-page">20</span></li>
      </ol>
      <footer class="footer">
        <span class="brand-name">Meridian Benefit Group</span>
      </footer>
    </main>
  </div>
</body>
</html>
```